PWR Business Card

Looking for a business card for my restaurant group I own. Four different concepts:

Copperleaf Alehouse
Bramble Alehouse
Hollister's Wood Fired Grill
Fenwick Patty Company

Card doesn't need to include all the logos.

```html
<!DOCTYPE html>
<html lang="en">
<head>
<meta charset="utf-8">
<title>PWR Business Card</title>
<link href="https://fonts.googleapis.com/css2?family=Open+Sans:wght@400;600;700&display=swap" rel="stylesheet">
<style>
  :root {
    --backdrop: #26272a;
    --card: #141415;
    --gold: #d6b46c;
    --white: #f4f4f2;
  }
  * { box-sizing: border-box; margin: 0; padding: 0; }
  html, body {
    width: 1200px;
    height: 900px;
    overflow: hidden;
    background: var(--backdrop);
    font-family: "Open Sans", sans-serif;
  }
  .card {
    position: absolute;
    left: 260px;
    width: 680px;
    height: 389px;
    background: var(--card);
    overflow: hidden;
  }
  .card--front { top: 40px; }
  .card--back { top: 471px; }

  .brand {
    position: absolute;
    display: flex;
    flex-direction: column;
    align-items: center;
    gap: 14px;
    color: var(--gold);
    font-weight: 600;
    text-transform: uppercase;
    text-align: center;
  }
  .brand__mark {
    width: 14px;
    height: 14px;
    background: var(--gold);
  }
  .brand__initials {
    font-size: 64px;
    letter-spacing: 6px;
    line-height: 1;
  }
  .brand__name {
    font-size: 15px;
    letter-spacing: 4px;
    line-height: 1.5;
  }
  .card--front .brand {
    left: 0;
    right: 0;
    top: 96px;
  }
  .card--back .brand {
    left: 40px;
    width: 300px;
    top: 112px;
  }
  .brand--small .brand__initials { font-size: 54px; }
  .brand--small .brand__name { font-size: 13px; letter-spacing: 3px; }

  .divider {
    position: absolute;
    left: 358px;
    top: 92px;
    width: 1.5px;
    height: 176px;
    background: var(--gold);
  }
  .contact {
    position: absolute;
    left: 384px;
    top: 96px;
    color: var(--white);
  }
  .contact__name {
    color: var(--gold);
    font-weight: 700;
    font-size: 22px;
    line-height: 1.2;
  }
  .contact__company {
    font-size: 15px;
    margin-top: 4px;
  }
  .contact__list {
    list-style: none;
    margin-top: 22px;
    display: flex;
    flex-direction: column;
    gap: 9px;
  }
  .contact__item {
    display: flex;
    align-items: center;
    gap: 12px;
    font-size: 15px;
  }
  .contact__icon {
    width: 14px;
    height: 14px;
    flex: none;
  }
  .band {
    position: absolute;
    left: 0;
    right: 0;
    bottom: 0;
    height: 14px;
    background: var(--gold);
  }
</style>
</head>
<body>
  <section class="card card--front">
    <div class="brand">
      <span class="brand__mark"></span>
      <span class="brand__initials">PWR</span>
      <span class="brand__name">Pinewater Hospitality Group</span>
    </div>
  </section>

  <section class="card card--back">
    <div class="brand brand--small">
      <span class="brand__mark"></span>
      <span class="brand__initials">PWR</span>
      <span class="brand__name">Pinewater Hospitality Group</span>
    </div>

    <span class="divider"></span>

    <div class="contact">
      <p class="contact__name">Dana Corliss</p>
      <p class="contact__company">Pinewater Hospitality Group</p>
      <ul class="contact__list">
        <li class="contact__item">
          <svg class="contact__icon" viewBox="0 0 16 16" aria-hidden="true">
            <path fill="#d6b46c" d="M3.2 1.5l2.3-.4 1.4 3.3-1.6 1.2c.8 1.8 2.2 3.2 4 4l1.2-1.6 3.3 1.4-.4 2.3c-.2.9-1 1.5-1.9 1.4C6.4 12.6 3.4 9.6 1.9 4.5c-.1-.9.4-1.8 1.3-3z"/>
          </svg>
          <span>555-014-2290</span>
        </li>
        <li class="contact__item">
          <svg class="contact__icon" viewBox="0 0 16 16" aria-hidden="true">
            <rect x="1" y="3" width="14" height="10" rx="1" fill="#d6b46c"/>
            <path d="M1.5 3.5L8 9l6.5-5.5" fill="none" stroke="#141415" stroke-width="1.4"/>
          </svg>
          <span>dana@pwrdining.com</span>
        </li>
        <li class="contact__item">
          <svg class="contact__icon" viewBox="0 0 16 16" aria-hidden="true">
            <circle cx="8" cy="8" r="6.5" fill="none" stroke="#d6b46c" stroke-width="1.5"/>
            <ellipse cx="8" cy="8" rx="2.8" ry="6.5" fill="none" stroke="#d6b46c" stroke-width="1.2"/>
            <path d="M1.5 8h13" stroke="#d6b46c" stroke-width="1.2"/>
          </svg>
          <span>www.pwrdining.com</span>
        </li>
      </ul>
    </div>

    <span class="band"></span>
  </section>
</body>
</html>
```